Bref créative
T&R FINANCIAL SERVICE
"Where Your Concern Is Our Focus"
Professional
Marisol Quade
2417 Birchwood Lane, Suite 208
P.O. Box 3782
Millbrook, AL 36197
support@trfinancialgroup.example
trfinancialgroup.example
please incorporate center logo from the website (the one with the green and black writing) thanks
for those who needed ai

```html
<!DOCTYPE html>
<html lang="en">
<head>
<meta charset="utf-8">
<title>T&amp;R Financial Service — Stationery</title>
<link rel="stylesheet" href="https://fonts.googleapis.com/css2?family=Open+Sans:wght@400;600;700&display=swap">
<style>
  :root{
    --bg:#e9e7e4;
    --paper:#ffffff;
    --green:#0f8a45;
    --green-dark:#064d27;
    --green-light:#22b05f;
    --black:#111111;
    --ink:#3a3a3a;
    --muted:#8a8a8a;
  }
  *{margin:0;padding:0;box-sizing:border-box}
  html,body{width:1200px;height:897px;overflow:hidden;background:var(--bg)}
  body{position:relative;font-family:"Open Sans",Arial,sans-serif;color:var(--ink)}
  .sheet{position:absolute;background:var(--paper);box-shadow:0 6px 18px rgba(0,0,0,.18);overflow:hidden}
  .sheet svg.art{position:absolute;left:0;bottom:0}
  .brand{display:flex;align-items:center;gap:7px}
  .brand-dot{border-radius:50%;background:var(--green);flex:none}
  .brand-name{font-weight:700;color:var(--green-dark);line-height:1.1;letter-spacing:.3px;white-space:nowrap}
  .address{font-size:9px;line-height:1.35;color:var(--ink);white-space:nowrap}

  /* Letterhead */
  .letterhead{left:97px;top:73px;width:460px;height:737px}
  .letterhead .brand{position:absolute;left:30px;top:34px}
  .letterhead .brand-dot{width:30px;height:30px}
  .letterhead .brand-name{font-size:10px}
  .letterhead .address{position:absolute;left:175px;top:30px}
  .letter-body{position:absolute;left:30px;top:118px;width:390px;font-size:7.4px;line-height:1.55;color:#666}
  .letter-body p{margin-bottom:9px}
  .letterhead .web{position:absolute;right:26px;bottom:14px;color:#fff;font-size:13px;font-weight:600}

  /* Business card */
  .card{left:605px;top:170px;width:545px;height:315px;border-radius:16px}
  .card .brand{position:absolute;left:34px;top:38px}
  .card .brand-dot{width:38px;height:38px}
  .card .brand-name{font-size:14px}
  .card .person{position:absolute;left:236px;top:32px;font-size:20px;font-weight:600;color:var(--green)}
  .card .rule{position:absolute;left:236px;top:62px;width:270px;height:1px;background:#bbb}
  .card .address{position:absolute;left:236px;top:72px;font-size:10.5px}
  .card .web{position:absolute;right:26px;bottom:22px;color:#fff;font-size:20px;font-weight:600}

  /* Envelope front */
  .envelope-front{left:605px;top:500px;width:545px;height:132px}
  .envelope-front .brand{position:absolute;left:30px;top:22px}
  .envelope-front .brand-dot{width:28px;height:28px}
  .envelope-front .brand-name{font-size:10px}
  .envelope-front .address{position:absolute;left:170px;top:20px;font-size:8px}

  /* Envelope back */
  .envelope-back{left:605px;top:645px;width:545px;height:200px}
  .flap-mark{position:absolute;left:236px;top:44px;width:72px;height:72px;border-radius:50%;border:2px solid #fff;display:flex;align-items:center;justify-content:center;text-align:center}
  .flap-mark span{font-size:8px;font-weight:700;color:#fff;line-height:1.1}
</style>
</head>
<body>

<section class="sheet letterhead">
  <div class="brand"><div class="brand-dot"></div><div class="brand-name">T&amp;R FINANCIAL<br>SERVICE</div></div>
  <div class="address">
    2417 Birchwood Lane, Suite 208<br>
    P.O. Box 3782<br>
    Millbrook, AL 36197<br>
    P: (334) 555-0148<br>
    E: support@trfinancialgroup.example
  </div>
  <div class="letter-body">
    <p>Recipient Full Name<br>14 Elm Road<br>Millbrook, AL</p>
    <p>Dear Valued Client,</p>
    <p>Thank you for choosing our firm to guide your financial planning this year. We review every account with care and keep you informed at each step of the process. Our advisors remain available for any question about savings, loans, insurance or retirement goals that matter to you.</p>
    <p>Enclosed you will find a summary of the services discussed during our recent meeting. Please read the notes carefully and mark any item you would like to change before the next review. We will follow up within two weeks to confirm the plan.</p>
    <p>Our office hours run Monday to Friday, and appointments can be booked by phone or email. We value your trust and look forward to helping you reach each financial goal with clarity and confidence.</p>
    <p>Should you need anything further, simply reply to this letter or visit our office in person.</p>
    <p>Yours sincerely,<br>Client Name</p>
  </div>
  <svg class="art" width="460" height="170" viewBox="0 0 460 170" aria-hidden="true">
    <defs>
      <linearGradient id="lhGreen" x1="0" y1="0" x2="0" y2="1">
        <stop offset="0" stop-color="var(--green-light)"/><stop offset="1" stop-color="var(--green-dark)"/>
      </linearGradient>
    </defs>
    <path d="M0 70 C120 20 300 10 460 40 L460 170 L0 170 Z" fill="var(--black)"/>
    <path d="M0 86 C130 36 300 30 460 58 L460 170 L0 170 Z" fill="#fff"/>
    <path d="M0 96 C130 50 300 42 460 68 L460 170 L0 170 Z" fill="url(#lhGreen)"/>
  </svg>
  <div class="web">trfinancialgroup.example</div>
</section>

<section class="sheet card">
  <div class="brand"><div class="brand-dot"></div><div class="brand-name">T&amp;R FINANCIAL<br>SERVICE</div></div>
  <div class="person">Marisol Quade</div>
  <div class="rule"></div>
  <div class="address">
    2417 Birchwood Lane, Suite 208<br>
    P.O. Box 3782<br>
    Millbrook, AL 36197<br>
    P: (334) 555-0148<br>
    E: support@trfinancialgroup.example
  </div>
  <svg class="art" width="545" height="140" viewBox="0 0 545 140" aria-hidden="true">
    <defs>
      <linearGradient id="cardGreen" x1="0" y1="0" x2="0" y2="1">
        <stop offset="0" stop-color="var(--green-light)"/><stop offset="1" stop-color="var(--green-dark)"/>
      </linearGradient>
    </defs>
    <path d="M0 80 C150 60 360 10 545 8 L545 140 L0 140 Z" fill="var(--black)"/>
    <path d="M0 96 C150 76 360 30 545 28 L545 140 L0 140 Z" fill="#fff"/>
    <path d="M0 104 C150 86 360 42 545 40 L545 140 L0 140 Z" fill="url(#cardGreen)"/>
  </svg>
  <div class="web">trfinancialgroup.example</div>
</section>

<section class="sheet envelope-front">
  <div class="brand"><div class="brand-dot"></div><div class="brand-name">T&amp;R FINANCIAL<br>SERVICE</div></div>
  <div class="address">
    2417 Birchwood Lane, Suite 208<br>
    P.O. Box 3782<br>
    Millbrook, AL 36197
  </div>
  <svg class="art" width="545" height="70" viewBox="0 0 545 70" aria-hidden="true">
    <path d="M120 70 C250 40 420 10 545 6 L545 70 Z" fill="var(--black)"/>
    <path d="M150 70 C270 48 430 22 545 18 L545 70 Z" fill="#fff"/>
    <path d="M170 70 C280 54 430 30 545 26 L545 70 Z" fill="var(--green)"/>
  </svg>
</section>

<section class="sheet envelope-back">
  <svg width="545" height="200" viewBox="0 0 545 200" aria-hidden="true" style="position:absolute;left:0;top:0">
    <defs>
      <linearGradient id="flapGreen" x1="0" y1="0" x2="0" y2="1">
        <stop offset="0" stop-color="var(--green-dark)"/><stop offset="1" stop-color="var(--green-light)"/>
      </linearGradient>
    </defs>
    <path d="M0 0 L545 0 L545 30 C470 80 380 140 272 142 C164 140 75 80 0 30 Z" fill="var(--black)"/>
    <path d="M0 0 L545 0 L545 22 C470 70 380 128 272 130 C164 128 75 70 0 22 Z" fill="#fff"/>
    <path d="M0 0 L545 0 L545 14 C470 62 380 118 272 120 C164 118 75 62 0 14 Z" fill="url(#flapGreen)"/>
  </svg>
  <div class="flap-mark"><span>T&amp;R FINANCIAL<br>SERVICE</span></div>
</section>

</body>
</html>
```